Business Card Design for Engineering Firm

Need a business card design for small mechanical and plumbing engineering form based in Utah. Design should be customizable for all employees.

```html
<!DOCTYPE html>
<html lang="en">
<head>
<meta charset="utf-8">
<title>Halvorsen Engineering – Business Card</title>
<link rel="stylesheet" href="https://fonts.googleapis.com/css2?family=Montserrat:wght@400;500;700&display=swap">
<style>
  :root {
    --brand-red: #7f1418;
    --brand-grey: #4b4b4d;
    --ink: #1e1e1e;
    --paper: #ffffff;
    --backdrop: #e8e8ea;
  }
  * { box-sizing: border-box; margin: 0; padding: 0; }
  html, body {
    width: 1200px; height: 900px; overflow: hidden;
    background: var(--backdrop);
    font-family: "Montserrat", Arial, sans-serif;
  }
  .sheet { position: relative; width: 1200px; height: 900px; }
  .card {
    position: absolute;
    width: 660px; height: 377px;
    background: var(--paper);
    box-shadow: 0 2px 10px rgba(0,0,0,0.12);
    overflow: hidden;
  }
  .card--front { left: 70px; top: 50px; }
  .card--back { left: 470px; top: 470px; }

  .wordmark {
    position: absolute;
    color: var(--brand-red);
    font-weight: 700;
    text-align: center;
    line-height: 1;
  }
  .wordmark__line { display: block; }
  .card--front .wordmark {
    left: 0; right: 0; top: 150px;
    font-size: 46px; letter-spacing: 1px;
  }
  .card--front .wordmark__sub {
    font-size: 20px; letter-spacing: 10px; margin-top: 10px;
  }
  .card--back .wordmark {
    left: 30px; width: 270px; top: 125px;
    font-size: 30px; letter-spacing: 0.5px;
  }
  .card--back .wordmark__sub {
    font-size: 13px; letter-spacing: 6.5px; margin-top: 8px;
  }

  .wave { position: absolute; inset: 0; }

  .divider {
    position: absolute; left: 318px; top: 62px;
    width: 1.5px; height: 170px; background: var(--brand-red);
  }
  .contact {
    position: absolute; left: 342px; top: 36px;
    color: var(--ink); font-size: 15px; font-weight: 500; line-height: 1.3;
  }
  .contact__name {
    font-size: 25px; font-weight: 700; color: var(--brand-grey);
    letter-spacing: 0.3px; line-height: 1.1;
  }
  .contact__name span { color: var(--brand-red); }
  .contact__role { margin-bottom: 10px; }
  .contact__address { margin-bottom: 10px; }
  .contact__row { display: flex; align-items: center; gap: 9px; margin-bottom: 2px; }
  .contact__icon { width: 16px; height: 16px; flex: none; }
</style>
</head>
<body>
<main class="sheet">

  <section class="card card--front" aria-label="Card front">
    <div class="wordmark">
      <span class="wordmark__line">HALVORSEN</span>
      <span class="wordmark__line wordmark__sub">ENGINEERING</span>
    </div>
  </section>

  <section class="card card--back" aria-label="Card back">
    <svg class="wave" viewBox="0 0 660 377" aria-hidden="true">
      <path d="M190 377 C320 300 450 310 565 258 C612 236 645 205 660 180 L660 377 Z" fill="var(--brand-grey)"/>
      <path d="M206 377 C332 308 462 322 572 270 C618 248 648 220 660 198 L660 377 Z" fill="var(--brand-red)"/>
    </svg>

    <div class="wordmark">
      <span class="wordmark__line">HALVORSEN</span>
      <span class="wordmark__line wordmark__sub">ENGINEERING</span>
    </div>

    <div class="divider"></div>

    <div class="contact">
      <p class="contact__name">EVAN <span>MARLOW</span></p>
      <p class="contact__role">Co-Founder</p>
      <p class="contact__address">P.O. Box 42-17 NTH-3<br>Cedar Lane 14, Riverton</p>
      <p class="contact__row">
        <svg class="contact__icon" viewBox="0 0 16 16" aria-hidden="true"><circle cx="8" cy="8" r="8" fill="var(--brand-red)"/><path d="M5.2 4.2l1.6-.3.8 2-1 .8a5.5 5.5 0 0 0 2.7 2.7l.8-1 2 .8-.3 1.6c-3.6.3-6.9-3-6.6-6.6z" fill="#fff"/></svg>
        801-555-0142
      </p>
      <p class="contact__row">
        <svg class="contact__icon" viewBox="0 0 16 16" aria-hidden="true"><circle cx="8" cy="8" r="8" fill="var(--brand-red)"/><rect x="4" y="5.2" width="8" height="5.6" fill="#fff"/><path d="M4 5.2l4 3 4-3" fill="none" stroke="var(--brand-red)" stroke-width="0.9"/></svg>
        info@halvorsen-eng.com
      </p>
      <p class="contact__row">
        <svg class="contact__icon" viewBox="0 0 16 16" aria-hidden="true"><circle cx="8" cy="8" r="8" fill="var(--brand-red)"/><circle cx="8" cy="8" r="4.2" fill="none" stroke="#fff" stroke-width="1"/><path d="M3.8 8h8.4M8 3.8c-2 2.4-2 6 0 8.4M8 3.8c2 2.4 2 6 0 8.4" fill="none" stroke="#fff" stroke-width="0.8"/></svg>
        www.halvorsen-eng.com
      </p>
    </div>
  </section>

</main>
</body>
</html>
```